Letterhead design for Dental Practice - Ashby Lane Dental Care

Letterhead for Private Dental Practice. To be used for all official correspondance and for printing treatment details on to be given to patients.

Target Market(s)

Private dental patients

Industry/Entity Type

Dental Clinic

Font styles to use
Other font styles liked:
• nexa-light

Colors
33a6d7
1c66ac
85abd2

Requirements
Must have
• info in the footer and header needs to be 3.5cm from upper/lower boader of paper, see photo in uploaded files
• info details:
• tel. 01632 960 418
• email info@ashbylanedc.co.uk
• ashbylanedentalcare.co.uk
• 17b Ashby Lane Fernbridge Marlow Vale MV4 2QT
• nexa-light font as in uploaded logo files
Should not have
• No funny tooth pictures

```html
<!DOCTYPE html>
<html lang="en">
<head>
<meta charset="utf-8">
<title>Ashby Lane Dental Care – Letterhead</title>
<link rel="stylesheet" href="https://fonts.googleapis.com/css2?family=Quicksand:wght@400;500&display=swap">
<style>
  :root {
    --brand-blue: #33a6d7;
    --brand-sky: #45c6ef;
    --brand-pale: #85abd2;
    --headline-grey: #7c7c7c;
    --body-grey: #5a5a5a;
    --footer-ink: #2b2b2b;
    --paper: #ffffff;
  }
  html, body {
    margin: 0;
    padding: 0;
    overflow: hidden;
    background: var(--paper);
  }
  .letterhead {
    position: relative;
    width: 849px;
    height: 1200px;
    overflow: hidden;
    background: var(--paper);
    font-family: "Quicksand", sans-serif;
  }
  .brand-name {
    position: absolute;
    left: 22px;
    top: 96px;
    margin: 0;
    font-size: 30px;
    font-weight: 400;
    line-height: 1.1;
    color: var(--brand-blue);
    text-transform: lowercase;
    letter-spacing: 0.5px;
  }
  .brand-name span { display: block; }
  .headline {
    position: absolute;
    left: 86px;
    top: 302px;
    margin: 0;
    font-weight: 400;
    font-size: 52px;
    line-height: 68px;
    letter-spacing: 3px;
    color: var(--headline-grey);
  }
  .headline span { display: block; }
  .letter-body {
    position: absolute;
    left: 89px;
    top: 460px;
    width: 682px;
    color: var(--body-grey);
    font-size: 17px;
    line-height: 21.5px;
    letter-spacing: 0.25px;
  }
  .letter-body p {
    margin: 0 0 8px;
    text-align: justify;
  }
  .signature {
    position: absolute;
    left: 551px;
    top: 870px;
    color: var(--headline-grey);
    font-size: 20px;
    line-height: 33px;
    letter-spacing: 0.6px;
  }
  .signature span { display: block; }
  .footer-contact,
  .footer-address {
    position: absolute;
    font-size: 10.5px;
    line-height: 17px;
    color: var(--footer-ink);
    font-weight: 500;
  }
  .footer-contact { left: 23px; top: 1113px; }
  .footer-address { left: 259px; top: 1131px; }
  .footer-contact span,
  .footer-address span { display: block; }
  .footer-divider {
    position: absolute;
    left: 219px;
    top: 1118px;
    width: 1px;
    height: 42px;
    background: var(--headline-grey);
  }
  .corner-accent {
    position: absolute;
    right: 0;
    bottom: 0;
    width: 250px;
    height: 220px;
  }
</style>
</head>
<body>
<div class="letterhead">
  <h1 class="brand-name"><span>ashby lane</span><span>dental care</span></h1>

  <h2 class="headline"><span>HEADLINE</span><span>LOREM IPSUM</span></h2>

  <div class="letter-body">
    <p>Lorem ipsum dolor sit amet, consectetuer adipiscing elit, sed diam nonummy nibh euismod tincidunt ut laoreet dolore magna aliquam erat volutpat. Ut wisi enim ad minim veniam, quis nostrud exerci tation ullamcorper suscipit lobortis nisl ut aliquip ex ea commodo consequat. Duis autem vel eum iriure dolor in hendrerit in vulputate velit esse molestie consequat, vel illum dolore eu feugiat nulla facilisis at vero eros et accumsan et iusto odio dignissim qui blandit praesent luptatum zzril delenit augue.</p>
    <p>Lorem ipsum dolor sit amet, consectetuer adipiscing elit, sed diam nonummy nibh euismod tincidunt ut laoreet dolore magna aliquam erat volutpat. Ut wisi enim ad minim veniam, quis nostrud exerci tation ullamcorper suscipit lobortis nisl ut aliquip ex ea commodo consequat. Duis autem vel eum iriure dolor in hendrerit in vulputate.</p>
    <p>Lorem ipsum dolor sit amet, consectetuer adipiscing elit, sed diam nonummy nibh euismod tincidunt ut laoreet dolore magna aliquam erat volutpat. Ut wisi enim ad minim veniam, quis nostrud exerci tation ullamcorper suscipit.</p>
  </div>

  <div class="signature"><span>GENERAL MANAGER</span><span>JOHN DOE</span></div>

  <div class="footer-contact">
    <span>01632 960 418</span>
    <span>info@ashbylanedc.co.uk</span>
    <span>ashbylanedentalcare.co.uk</span>
  </div>
  <div class="footer-divider"></div>
  <div class="footer-address">
    <span>17b Ashby Lane Fernbridge</span>
    <span>Marlow Vale MV4 2QT</span>
  </div>

  <svg class="corner-accent" viewBox="0 0 250 220" aria-hidden="true">
    <defs>
      <linearGradient id="accent-fade" x1="0" y1="1" x2="1" y2="0">
        <stop offset="0" stop-color="var(--brand-blue)"/>
        <stop offset="1" stop-color="var(--brand-pale)"/>
      </linearGradient>
    </defs>
    <path d="M30 220 Q120 120 250 70 L250 220 Z" fill="url(#accent-fade)"/>
  </svg>
</div>
</body>
</html>
```